Sheep ranch business card design

We need a business card design for our farm. We do all things sheep. We run Babydoll southdown sheep and use their fiber and meat. In the spring the lambs are sold. We shear them for their wool to make dryer balls, roving, and yarn which we sell. We also lease the sheep out to organic vineyards in the winter time to help them convert their weeds and cover crops to manure so they don't have to use tractors and tillers to mow and compact soil. Copperfield Ranch also breeds Kangals which are livestock guard dogs that live with and protect the sheep. We also run a small herd of jersey cows, chickens, and bees but the sheep enterprise is the focal point. I would like to see the design use more earth tones and natural colors and have the feel of a modern and hip farm. I would also like our attached copperfield ranch image to be used. The font family is dalle for our logo. That font can be used or something to compliment it. The attached pictures can be used as well but they are not necessary. One copperfield ranch upload is in psd and one is in jpeg. Thank You and we look forward to seeing your work.
Updates

So many great designs. Not looking for anything "western." Font, design, or otherwise.

Industry/Entity Type

Livestock

Contact Information for Business Card

Copperfield Ranch
Tessa Pollard
www.copperfieldranch.example
copperfieldranch@mailbox.example
phone: 555 210-7389

```html
<!DOCTYPE html>
<html lang="en">
<head>
<meta charset="utf-8">
<title>Copperfield Ranch – Business Card</title>
<link rel="stylesheet" href="https://fonts.googleapis.com/css2?family=Raleway:wght@400&display=swap">
<style>
  :root {
    --backdrop: #e9e7e3;
    --card-white: #f8f8f6;
    --green-deep: #4f8a22;
    --green-mid: #68a532;
    --green-light: #8cc152;
    --ink: #2f2f2f;
    --on-green: #f4f8ee;
  }
  * { margin: 0; padding: 0; box-sizing: border-box; }
  html, body {
    width: 1200px;
    height: 873px;
    overflow: hidden;
    background: var(--backdrop);
    font-family: "Raleway", "Helvetica Neue", Arial, sans-serif;
  }
  .canvas {
    position: relative;
    width: 1200px;
    height: 873px;
  }
  .business-card {
    position: absolute;
    left: 180px;
    top: 196px;
    width: 840px;
    height: 480px;
    background: var(--card-white);
    overflow: hidden;
    box-shadow: 0 6px 24px rgba(0, 0, 0, 0.12);
  }
  .card-swoosh {
    position: absolute;
    inset: 0;
    width: 100%;
    height: 100%;
  }
  .brand {
    position: absolute;
    top: 46px;
    right: 48px;
    display: flex;
    align-items: center;
    gap: 14px;
    color: var(--ink);
  }
  .brand-dot {
    width: 22px;
    height: 22px;
    border-radius: 50%;
    background: var(--ink);
  }
  .brand-name {
    font-size: 34px;
    font-weight: 400;
    letter-spacing: 0.14em;
    text-transform: uppercase;
  }
  .contact {
    position: absolute;
    left: 420px;
    top: 292px;
    color: var(--on-green);
    text-transform: uppercase;
  }
  .contact-name {
    font-size: 30px;
    font-weight: 400;
    letter-spacing: 0.06em;
    margin-bottom: 22px;
  }
  .contact-lines {
    list-style: none;
    font-size: 16px;
    letter-spacing: 0.05em;
    line-height: 1.55;
  }
</style>
</head>
<body>
<main class="canvas">
  <section class="business-card" aria-label="Copperfield Ranch business card">
    <svg class="card-swoosh" viewBox="0 0 840 480" preserveAspectRatio="none" aria-hidden="true">
      <defs>
        <radialGradient id="swoosh-main" cx="0.55" cy="0.7" r="0.8">
          <stop offset="0" stop-color="var(--green-mid)"/>
          <stop offset="1" stop-color="var(--green-deep)"/>
        </radialGradient>
        <linearGradient id="swoosh-lobe" x1="0" y1="0" x2="1" y2="1">
          <stop offset="0" stop-color="var(--green-deep)"/>
          <stop offset="1" stop-color="var(--green-light)"/>
        </linearGradient>
      </defs>
      <path d="M0 0 H300 C300 120 200 190 0 230 Z" fill="url(#swoosh-lobe)"/>
      <path d="M0 0 H300 C330 150 480 210 840 250 V480 H0 Z" fill="url(#swoosh-main)"/>
      <path d="M0 230 C200 190 300 120 300 0 C330 150 480 210 840 250 C520 235 250 215 0 300 Z" fill="var(--green-light)" opacity="0.18"/>
    </svg>

    <div class="brand">
      <span class="brand-dot"></span>
      <span class="brand-name">Copperfield Ranch</span>
    </div>

    <div class="contact">
      <p class="contact-name">Tessa Pollard</p>
      <ul class="contact-lines">
        <li>555 210-7389</li>
        <li>www.copperfieldranch.example</li>
        <li>copperfieldranch@mailbox.example</li>
      </ul>
    </div>
  </section>
</main>
</body>
</html>
```